Gin bottle designs - micro distillery

We are an Italian Distillery in Melbourne Australia. We would like to modernise the brand and in particular the bottle labels. We need to get a lable that will look better on the shelf while still maintaining the Italian "feel" of the product.

You can also refer to web site: www.verantocellars.com for a background.

At this time we are stuck with the rectangular bottles. We can consider different configurations (like a top label and a wrap around label at the bottom

The key message is more modern and attention grabbing.

Target Market(s)

Alcohol drinkers

Requirements
Must have
• GIN
Mediterranean Gin
Grappa
Brandy
Vodka

```html
<!DOCTYPE html>
<html lang="en">
<head>
<meta charset="utf-8">
<title>Veranto Mediterranean Gin – Label</title>
<link href="https://fonts.googleapis.com/css2?family=Cinzel:wght@400;700&family=Lato:ital,wght@0,300;1,400&display=swap" rel="stylesheet">
<style>
  :root {
    --page-bg: #f4f4f4;
    --label-black: #1b1b1b;
    --ink-white: #ffffff;
    --vine-green: #4bb34f;
    --grape-green-light: #6fd06b;
    --grape-green-dark: #2f7d33;
    --flag-red: #e0533d;
    --band-white: #ffffff;
    --band-text: #1b1b1b;
  }
  * { margin: 0; padding: 0; box-sizing: border-box; }
  html, body {
    width: 1200px; height: 2400px; overflow: hidden;
    background: var(--page-bg);
  }
  .label {
    position: absolute; left: 215px; top: 181px;
    width: 770px; height: 2037px;
    background: var(--label-black);
    color: var(--ink-white);
    box-shadow: 0 30px 50px rgba(0,0,0,0.25);
  }
  .centered { position: absolute; left: 0; width: 100%; text-align: center; }

  .brand-mark {
    top: 230px;
    display: flex; justify-content: center; align-items: center; gap: 22px;
  }
  .brand-mark__square {
    width: 40px; height: 40px; background: var(--flag-red);
  }
  .brand-mark__name {
    font-family: "Cinzel", serif; font-weight: 700;
    font-size: 72px; letter-spacing: 4px; color: var(--ink-white);
  }

  .product-kind {
    top: 525px;
    font-family: "Cinzel", serif; font-weight: 400;
    font-size: 50px; letter-spacing: 1px; line-height: 60px;
  }
  .product-name {
    top: 575px;
    font-family: "Cinzel", serif; font-weight: 700;
    font-size: 232px; line-height: 240px; letter-spacing: -4px;
  }

  .grape-illustration {
    position: absolute; left: 78px; top: 850px;
    width: 605px; height: 375px;
    background: radial-gradient(ellipse at 45% 55%, var(--grape-green-light) 0%, var(--grape-green-dark) 55%, rgba(27,27,27,0) 75%);
    opacity: 0.85;
  }

  .claims {
    font-family: "Lato", sans-serif; font-style: italic; font-weight: 400;
    font-size: 33px; line-height: 36px;
  }
  .claims--grape { top: 1282px; }
  .claims--botanicals { top: 1427px; }
  .claims--origin { top: 1602px; }
  .divider {
    position: absolute; left: 300px; width: 170px; height: 3px;
    background: linear-gradient(90deg, rgba(75,179,79,0), var(--vine-green), rgba(75,179,79,0));
  }
  .divider--first { top: 1394px; }
  .divider--second { top: 1569px; }

  .heritage-band {
    position: absolute; left: 0; top: 1737px; width: 100%; height: 80px;
    display: flex; flex-direction: column;
  }
  .heritage-band__red { height: 12px; background: var(--flag-red); }
  .heritage-band__white {
    height: 55px; background: var(--band-white);
    display: flex; align-items: center; justify-content: center;
    font-family: "Cinzel", serif; font-weight: 700;
    font-size: 28px; color: var(--band-text); letter-spacing: 0.5px;
  }
  .heritage-band__green { height: 13px; background: var(--vine-green); }

  .volume {
    font-family: "Lato", sans-serif; font-weight: 300;
    font-size: 40px; line-height: 58px;
  }
  .volume { top: 1875px; }
</style>
</head>
<body>
  <main class="label">
    <div class="centered brand-mark">
      <span class="brand-mark__square"></span>
      <span class="brand-mark__name">VERANTO</span>
    </div>

    <p class="centered product-kind">MEDITERRANEAN</p>
    <h1 class="centered product-name">GIN</h1>

    <div class="grape-illustration" role="img" aria-label="Green line drawing of a bunch of grapes with a vine leaf"></div>

    <p class="centered claims claims--grape">Made from Premium<br>Australian Grape Spirit</p>
    <span class="divider divider--first"></span>
    <p class="centered claims claims--botanicals">Distilled With Lavender,<br>Rosemary, Fennel &amp; Other Select<br>Mediterraneam Botanicals</p>
    <span class="divider divider--second"></span>
    <p class="centered claims claims--origin">Handmade and Bottled<br>in Melbourne, Australia</p>

    <div class="heritage-band">
      <div class="heritage-band__red"></div>
      <div class="heritage-band__white">ITALIAN HERITAGE AUSSIE SPIRIT</div>
      <div class="heritage-band__green"></div>
    </div>

    <p class="centered volume">500 ml<br>45% ALC/VOL</p>
  </main>
</body>
</html>
```